New Alcoholic Spiked Seltzer Line

We need a can design for a line of low calorie alcoholic seltzer. This product is a sparkling water and vodka drink with no sugar added in a slim 12 oz can.

This is a lighter, healthier, alternative to the sugary ready-to-drinks on the market. The product contains only 3 ingredients: Vodka, Water and Natural Flavors. It has only 100 calories but still has 5% alcohol, so you don't need to sacrifice alcohol to cut calories.

This product also does not contain any preservatives.

We want this design to communicate the following objectives to the consumer and in this order:

1. Appetizing product
2.Low calorie
3.Communicate the type of beverage (Spiked Seltzer)

The brand name of the product is VELKA.

The flavor of the product needed to be used for the design is Mango-Orange.

Comparable products are:

www.brisavelfizz.example/
https://www.tarnowbubble.example
https://quellrind.example/

The designs should not infringe or copy the creative directions of the products mentionned above. They are only given so that you can better understand the type of product we are developing.

Target Market(s)

Young Professional women between the ages of 25 and 44

Industry/Entity Type

Product

Colors

Designer to choose colors to be used in the design.

Requirements
Must have
• Design extendibility, meaning it can be adapted for other flavors.
• This is a new category in the market we are targeting, so consumers must easily be able to identify what type of product this is.

```html
<!DOCTYPE html>
<html lang="en">
<head>
<meta charset="utf-8">
<title>VELKA Mango-Orange Spiked Seltzer – low calorie, 5% alc. vol.</title>
<link rel="stylesheet" href="https://fonts.googleapis.com/css2?family=Cinzel:wght@400;700&family=Roboto:wght@700;900&display=swap">
<style>
  :root {
    --backdrop: #9b9b9b;
    --label-white: #f7f7f6;
    --ink-black: #111111;
    --amber-deep: #8a5416;
    --amber: #b3701e;
    --orange-bright: #f29a1c;
    --orange-deep: #d4620f;
    --orange-peel: #f5a623;
    --mango-yellow: #f7c52a;
    --mango-red: #b8452a;
    --leaf-green: #3f7a2a;
    --water-light: #e8eef2;
    --band-orange: #e39a2a;
  }
  * { margin: 0; padding: 0; box-sizing: border-box; }
  html, body {
    width: 1200px;
    height: 2695px;
    overflow: hidden;
    background: var(--backdrop);
  }
  .label {
    position: absolute;
    left: 160px;
    top: 180px;
    width: 880px;
    height: 2210px;
    background: var(--label-white);
    overflow: hidden;
  }

  /* juice splashes */
  .splash-top {
    position: absolute;
    left: 90px; top: 110px;
    width: 738px; height: 270px;
    background: radial-gradient(ellipse at 50% 90%, rgba(242,154,28,0.85), rgba(247,197,42,0.35) 55%, rgba(255,255,255,0) 75%);
  }
  .splash-side {
    position: absolute;
    left: 0; top: 300px;
    width: 84px; height: 1010px;
    background: linear-gradient(180deg, var(--orange-bright), var(--orange-deep) 45%, var(--mango-yellow) 80%, rgba(247,197,42,0.15));
  }
  .splash-right {
    position: absolute;
    left: 830px; top: 600px;
    width: 50px; height: 340px;
    background: linear-gradient(180deg, rgba(242,154,28,0.3), var(--orange-bright) 50%, rgba(242,154,28,0.3));
  }

  .logo-frame {
    position: absolute;
    left: 0; top: 0;
    width: 880px; height: 1300px;
  }

  /* brand block */
  .brand-name {
    position: absolute;
    left: 150px; top: 440px;
    font-family: "Roboto", sans-serif;
    font-weight: 900;
    font-size: 176px;
    line-height: 1;
    letter-spacing: 4px;
    color: var(--ink-black);
  }
  .fruit {
    position: absolute;
    border-radius: 50%;
  }
  .fruit-orange {
    left: 190px; top: 720px;
    width: 250px; height: 240px;
    background: radial-gradient(circle at 40% 38%, #ffd27a, var(--orange-peel) 45%, var(--orange-deep) 100%);
  }
  .fruit-mango {
    left: 480px; top: 715px;
    width: 230px; height: 250px;
    border-radius: 48% 52% 46% 54% / 58% 58% 42% 42%;
    background: radial-gradient(circle at 45% 40%, #ffe27a, var(--mango-yellow) 50%, #e0901c 100%);
  }

  .product-type {
    position: absolute;
    left: 0; width: 880px;
    top: 1065px;
    text-align: center;
    font-family: "Cinzel", serif;
    font-weight: 400;
    font-size: 74px;
    line-height: 1;
    color: var(--ink-black);
  }

  /* facts */
  .abv {
    position: absolute;
    left: 0; width: 880px;
    top: 1375px;
    text-align: center;
    font-family: "Roboto", sans-serif;
    font-weight: 700;
    color: var(--amber-deep);
  }
  .abv-value { display: block; font-size: 140px; line-height: 1; }
  .abv-unit { display: block; font-size: 40px; line-height: 1.15; }
  .volume {
    position: absolute;
    left: 0; width: 880px;
    top: 1590px;
    text-align: center;
    font-family: "Cinzel", serif;
    font-weight: 700;
    font-size: 66px;
    line-height: 1;
    color: var(--amber);
  }
  .description {
    position: absolute;
    left: 0; width: 880px;
    top: 1670px;
    text-align: center;
    font-family: "Cinzel", serif;
    font-weight: 700;
    font-size: 46px;
    line-height: 72px;
    color: var(--ink-black);
  }

  /* bottom fruit scene */
  .fruit-splash {
    position: absolute;
    left: 0; top: 1865px;
    width: 880px; height: 288px;
    background:
      radial-gradient(ellipse 150px 120px at 250px 180px, var(--orange-peel), rgba(245,166,35,0) 100%),
      radial-gradient(ellipse 150px 120px at 110px 240px, var(--orange-deep), rgba(212,98,15,0) 100%),
      radial-gradient(ellipse 130px 120px at 600px 190px, var(--mango-red), rgba(184,69,42,0) 100%),
      radial-gradient(ellipse 120px 110px at 760px 200px, var(--mango-yellow), rgba(247,197,42,0) 100%),
      linear-gradient(180deg, var(--label-white), var(--water-light));
  }
  .base-band {
    position: absolute;
    left: 0; top: 2153px;
    width: 880px; height: 22px;
    background: var(--band-orange);
  }
</style>
</head>
<body>
  <main class="label">
    <div class="splash-top" role="img" aria-label="Orange and mango juice splash with flying droplets"></div>
    <div class="splash-side" role="img" aria-label="Vertical strip of splashing orange juice"></div>
    <div class="splash-right" role="img" aria-label="Edge of a mango-orange juice splash"></div>

    <svg class="logo-frame" viewBox="0 0 880 1300" aria-hidden="true">
      <g fill="none" stroke="#ffffff" stroke-width="8">
        <rect x="90" y="372" width="745" height="775"/>
        <line x1="90" y1="1070" x2="160" y2="1000"/>
        <line x1="90" y1="1110" x2="200" y2="1000"/>
        <line x1="96" y1="1144" x2="240" y2="1000"/>
      </g>
    </svg>

    <div class="brand-name">VELKA</div>
    <div class="fruit fruit-orange" role="img" aria-label="Fresh orange with a cut half and green leaf"></div>
    <div class="fruit fruit-mango" role="img" aria-label="Ripe mango with sliced pieces and leaf"></div>

    <div class="product-type">Spiked Seltzer</div>

    <div class="abv">
      <span class="abv-value">5%</span>
      <span class="abv-unit">Alc. Vol.</span>
    </div>

    <div class="volume">12 FL.OZ.(355ML.)</div>
    <div class="description">Alcoholic Spiked Seltzer with<br>Natural Flavour</div>

    <div class="fruit-splash" role="img" aria-label="Orange and mango halves splashing into sparkling water"></div>
    <div class="base-band"></div>
  </main>
</body>
</html>
```